Nice, modern, and professional credit repair website

We're a new credit repair company and we need a website to inform our prospective clients about the service we provide. We wan't it to catch the attention of the people as well as it be informative of the different types of derogatory items that can be listed on a report. Please refer to ( www.pathtoprime.example ) for an idea of what I'm looking for.

Colors
0455a3
0293ce
33a6d7
ffffff

Requirements
Must have
• The website must include information regarding credit repair. We'd like the website to include modern colors similar to that of our logo.
A link to our Facebook page. Www.facebook.example/veltrusfinancialrepair
A link to our Instagram page: @VeltrusFinancialRepair
A link to our Snapchat page: Veltrus-Repair
Also, we'd like to have an area where clients would fill out basic information where we could reach out to them.
Nice to have
• Images of new homes, cars, credit cards (Should NOT endorse Plixa, QB, ORVU, or Tremando.)

```html
<!DOCTYPE html>
<html lang="en">
<head>
<meta charset="utf-8">
<title>Veltrus Financial Repair</title>
<link href="https://fonts.googleapis.com/css2?family=Hind:wght@500;600;700&family=Lato:wght@400;700&display=swap" rel="stylesheet">
<style>
:root{
  --navy:#0455a3;
  --blue:#0293ce;
  --sky:#33a6d7;
  --pale:#c5e4f3;
  --ink:#1c1c1c;
  --muted:#6b6b6b;
  --white:#ffffff;
  --line:#e9eef2;
}
*{box-sizing:border-box;margin:0;padding:0}
html,body{width:1200px;height:4082px;overflow:hidden}
body{position:relative;background:var(--white);font-family:"Lato",sans-serif;color:var(--ink)}
.abs{position:absolute}
h1,h2,h3,.brand,.btn,.nav a{font-family:"Hind",sans-serif}
.eyebrow{font-family:"Hind",sans-serif;font-weight:700;font-size:13px;letter-spacing:.3px;color:var(--blue);text-transform:uppercase}
h2{font-weight:600;font-size:35px;line-height:42px;color:var(--ink)}
.copy{font-size:11.5px;line-height:21px;color:var(--muted)}
.btn{display:flex;align-items:center;justify-content:center;border-radius:30px;background:var(--navy);color:var(--white);font-weight:600;font-size:15px;text-decoration:none}
.center{left:0;width:1200px;text-align:center}

/* header */
.site-header{left:0;top:0;width:1095px;height:75px;background:var(--white);border-bottom-right-radius:40px;z-index:3}
.brand{display:flex;align-items:center;gap:8px;text-decoration:none}
.brand-mark{width:48px;height:48px;border-radius:50%;border:3px solid var(--navy)}
.brand-name{font-weight:700;font-size:30px;line-height:28px;color:var(--navy)}
.brand-sub{display:block;font-size:10px;letter-spacing:3px;line-height:12px}
.nav{left:462px;top:28px;display:flex;gap:28px}
.nav a{font-size:12px;color:#555;text-decoration:none;font-weight:500}
.header-cta{left:926px;top:20px;width:112px;height:36px;background:var(--sky);font-size:13px}

/* hero */
.hero-text{left:163px;color:var(--white)}
.hero h1{font-weight:600;font-size:48px;line-height:57px}
.hero-btn{left:161px;top:398px;width:330px;height:59px;background:var(--white);color:var(--navy);font-size:18px}

/* service cards */
.card{background:var(--white);border:1px solid var(--line);border-radius:8px;box-shadow:0 2px 10px rgba(0,0,0,.04);padding:0 18px;overflow:hidden}
.card .blob{position:absolute;left:0;top:0;width:60px;height:52px;background:var(--pale);border-radius:0 0 40px 0}
.card svg.icon{position:absolute;left:16px;top:40px}
.card h3{position:absolute;left:18px;font-size:15px;font-weight:600}
.card p{position:absolute;left:18px;right:14px;font-size:10.5px;line-height:21px;color:var(--muted)}

/* faq */
.faq-item{left:161px;width:375px;height:44px;background:var(--sky);color:var(--white);font-size:11px;font-weight:700;display:flex;align-items:center;padding-left:14px;border-radius:2px}
.faq-item span{font-size:16px;margin-right:8px;font-weight:400}
.faq-body{left:161px;top:2015px;width:375px;height:100px;border:1px solid var(--line);border-top:0;padding:16px 16px;font-size:10.5px;line-height:19px;color:var(--muted)}

/* steps */
.step-ring{width:82px;height:82px;border-radius:50%;border:2px solid var(--sky);display:flex;align-items:center;justify-content:center}
.step-ring div{width:64px;height:64px;border-radius:50%;border:1px solid #b8def0;display:flex;align-items:center;justify-content:center}
.step-label{font-weight:700;font-size:13px;text-align:center;width:200px}

/* footer */
.footer-col h3{font-size:16px;font-weight:600;color:var(--white);margin-bottom:14px}
.footer-col ul{list-style:none}
.footer-col li{font-size:11px;color:var(--white);line-height:22.5px}
.footer-col li::before{content:"";display:inline-block;width:4px;height:4px;background:var(--white);border-radius:50%;margin-right:12px;vertical-align:middle}
.social{width:36px;height:36px;border-radius:50%;border:1.5px solid var(--white);display:block}
.contact-row{display:flex;align-items:flex-start;gap:18px;font-size:11px;line-height:22px;color:var(--white);margin-bottom:18px}
</style>
</head>
<body>

<header class="abs site-header">
  <a class="abs brand" style="left:165px;top:12px" href="#">
    <span class="brand-mark"></span>
    <span class="brand-name">VELTRUS<span class="brand-sub">FINANCIAL REPAIR</span></span>
  </a>
  <nav class="abs nav">
    <a href="#">Home</a><a href="#">About Us</a><a href="#">Services</a><a href="#">Blog</a><a href="#">Pricing</a><a href="#">Contact Us</a>
  </nav>
  <a class="abs btn header-cta" href="#">Contact Us</a>
</header>

<section class="hero">
  <svg class="abs" style="left:0;top:0" width="1200" height="660" viewBox="0 0 1200 660">
    <defs>
      <linearGradient id="heroBlue" x1="0" y1="0" x2="1" y2="1">
        <stop offset="0" stop-color="#0455a3"/><stop offset=".6" stop-color="#1a86c8"/><stop offset="1" stop-color="#33a6d7"/>
      </linearGradient>
      <linearGradient id="heroPhoto" x1="0" y1="0" x2="1" y2="1">
        <stop offset="0" stop-color="#3a3a44"/><stop offset=".5" stop-color="#6b5a58"/><stop offset="1" stop-color="#c9b7b4"/>
      </linearGradient>
    </defs>
    <path role="img" aria-label="Photo of a woman holding a credit card while shopping on a laptop" fill="url(#heroPhoto)" d="M560 75 H1200 V655 C1100 640 1000 665 900 640 C780 610 680 590 560 560 Z"/>
    <path fill="url(#heroBlue)" d="M0 75 H850 C790 140 740 200 720 270 C700 330 650 360 600 420 C560 470 590 560 520 620 C450 660 380 610 300 520 C230 460 120 430 0 415 Z"/>
  </svg>
  <p class="abs hero-text eyebrow" style="top:158px;color:var(--white)">Get the results you need to improve your credit</p>
  <h1 class="abs hero-text" style="top:190px">Repair Your Credit With The<br>Experts</h1>
  <p class="abs hero-text" style="top:308px;font-size:11.5px;line-height:22px">Lorem Ipsum is simply dummy text of the printing and typesetting industry. Lorem<br>Ipsum has been the industry's standard dummy text ever since the 1500s</p>
  <a class="abs btn hero-btn" href="#">Schedule A Free Consultation</a>
</section>

<section class="services">
  <p class="abs eyebrow" style="left:163px;top:834px">How we can help you</p>
  <h2 class="abs" style="left:163px;top:858px">We Help Improve Your<br>Credit Scores</h2>
  <p class="abs copy" style="left:163px;top:952px;width:350px">Lorem Ipsum is simply dummy text of the printing and typesetting industry. Lorem Ipsum has been the industry's standard dummy text ever since the 1500s, when an unknown printer took a galley of typeand scrambled it to make a type specimen book.</p>
  <a class="abs btn" style="left:161px;top:1073px;width:150px;height:44px;font-size:14px" href="#">More Services</a>

  <article class="abs card" style="left:560px;top:845px;width:278px;height:262px">
    <span class="blob"></span>
    <svg class="icon" width="64" height="56" viewBox="0 0 64 56" fill="none" stroke="#0455a3" stroke-width="2.5"><path d="M6 38 V28 L14 12 H44 L54 28 V38 Z M14 28 H54"/><circle cx="18" cy="40" r="6"/><circle cx="44" cy="40" r="6"/></svg>
    <h3 style="top:120px">Repossessions</h3>
    <p style="top:146px">Lorem Ipsum is simply dummy text of the printing and typesetting industry. Lorem Ipsum has been the industry's standard dummy text ever since the 1500s.</p>
  </article>
  <article class="abs card" style="left:860px;top:702px;width:278px;height:263px">
    <span class="blob"></span>
    <svg class="icon" width="60" height="56" viewBox="0 0 60 56" fill="none" stroke="#0455a3" stroke-width="2.5"><rect x="4" y="16" width="46" height="34"/><path d="M12 16 L30 4 L40 16"/><text x="10" y="42" font-size="18" fill="#0455a3" stroke="none" font-family="Hind,sans-serif" font-weight="700">$</text><rect x="28" y="26" width="18" height="14" rx="2"/></svg>
    <h3 style="top:120px">Late payments</h3>
    <p style="top:146px">Lorem Ipsum is simply dummy text of the printing and typesetting industry. Lorem Ipsum has been the industry's standard dummy text ever since the 1500s.</p>
  </article>
  <article class="abs card" style="left:860px;top:988px;width:278px;height:263px">
    <span class="blob"></span>
    <svg class="icon" width="60" height="56" viewBox="0 0 60 56" fill="none" stroke="#0455a3" stroke-width="2.5"><path d="M4 8 H22 L28 14 H54 V50 H4 Z"/><circle cx="30" cy="28" r="6"/><path d="M20 44 C22 36 38 36 40 44"/></svg>
    <h3 style="top:120px">Collection Accounts</h3>
    <p style="top:146px">Lorem Ipsum is simply dummy text of the printing and typesetting industry. Lorem Ipsum has been the industry's standard dummy text ever since the 1500s.</p>
  </article>
</section>

<section class="guarantee">
  <svg class="abs" style="left:0;top:1215px" width="510" height="535" viewBox="0 0 510 535">
    <defs><linearGradient id="truck" x1="0" y1="0" x2="1" y2="1"><stop offset="0" stop-color="#4a3c38"/><stop offset=".6" stop-color="#2a2a2e"/><stop offset="1" stop-color="#121216"/></linearGradient></defs>
    <path d="M0 60 C100 20 260 -10 380 10 C480 30 520 130 490 220 C460 300 390 340 370 420 C350 500 290 545 220 520 C140 495 60 440 0 400 Z" fill="none" stroke="#0455a3" stroke-width="1.5" transform="translate(8 8)"/>
    <path role="img" aria-label="Photo of a pickup truck at dusk" fill="url(#truck)" d="M0 60 C100 20 260 -10 380 10 C480 30 520 130 490 220 C460 300 390 340 370 420 C350 500 290 545 220 520 C140 495 60 440 0 400 Z"/>
    <circle cx="242" cy="428" r="20" fill="none" stroke="#fff" stroke-width="2.5"/>
    <path d="M236 418 L252 428 L236 438 Z" fill="none" stroke="#fff" stroke-width="2.5"/>
  </svg>
  <p class="abs eyebrow" style="left:612px;top:1342px">Worries, begone!</p>
  <h2 class="abs" style="left:612px;top:1366px">We Have The Best 100%<br>Money Back Guarantee</h2>
  <p class="abs copy" style="left:612px;top:1461px;width:330px">If you have not received any improvement within 6 months of service from your enrollment date, we'll refund your money – including your enrollment fee. No questions asked!</p>
  <a class="abs btn" style="left:612px;top:1582px;width:148px;height:43px;font-size:14px" href="#">Explore Now</a>
</section>

<section class="faq">
  <svg class="abs" style="left:700px;top:1700px" width="500" height="675" viewBox="0 0 500 675">
    <defs><linearGradient id="circ" x1="0" y1="0" x2="1" y2="1"><stop offset="0" stop-color="#0293ce"/><stop offset="1" stop-color="#0455a3"/></linearGradient></defs>
    <circle cx="510" cy="88" r="75" fill="url(#circ)"/>
    <path d="M220 30 C320 -10 440 60 500 120 V670 C380 680 200 660 110 590 C20 520 -10 400 20 260 C40 160 120 70 220 30 Z" fill="none" stroke="#0455a3" stroke-width="1.5"/>
    <path role="img" aria-label="Photo of two smiling business professionals in suits" fill="#eef2f6" d="M220 40 C320 0 430 70 490 130 V665 C380 672 210 650 120 585 C30 520 0 400 30 265 C50 165 125 80 220 40 Z"/>
    <rect x="130" y="70" width="300" height="600" fill="#22262e" opacity=".18" rx="120"/>
  </svg>
  <p class="abs eyebrow" style="left:163px;top:1822px">Veltrus Financial Repair</p>
  <h2 class="abs" style="left:163px;top:1843px;font-size:31px">Frequently Asked Questions</h2>
  <div class="abs faq-item" style="top:1910px"><span>+</span>Is Credit Repair legal?</div>
  <div class="abs faq-item" style="top:1972px"><span>–</span>Is Credit Repair and Education worth my time and money?</div>
  <div class="abs faq-body">Lorem Ipsum is simply dummy text of the printing and typesetting industry. Lorem Ipsum has been the industry's standard dummy text ever since the 1500s.</div>
  <div class="abs faq-item" style="top:2136px"><span>+</span>What is your 100% Guarantee?</div>
  <div class="abs faq-item" style="top:2196px"><span>+</span>How long will it take to raise my score?</div>
</section>

<section class="why">
  <p class="abs eyebrow center" style="top:2355px">Why us?</p>
  <h2 class="abs center" style="top:2375px;font-size:34px">Why Veltrus Financial Repair</h2>
  <p class="abs copy center" style="top:2430px;left:340px;width:520px">Lorem Ipsum is simply dummy text of the printing and typesetting industry. Lorem Ipsum has been the industry's standard dummy text ever since the 1500s, when an unknown printer took a galley of typeand scrambled it to make a type specimen book.</p>
  <svg class="abs" style="left:343px;top:2562px" width="512" height="2"><line x1="0" y1="1" x2="512" y2="1" stroke="#33a6d7" stroke-dasharray="2 4"/></svg>
  <div class="abs step-ring" style="left:261px;top:2522px"><div><svg width="30" height="34" viewBox="0 0 30 34" fill="none" stroke="#33a6d7" stroke-width="2"><rect x="3" y="2" width="24" height="30" rx="2"/><circle cx="15" cy="14" r="4"/><path d="M9 26 C10 20 20 20 21 26"/></svg></div></div>
  <div class="abs step-ring" style="left:557px;top:2522px"><div><svg width="30" height="34" viewBox="0 0 30 34" fill="none" stroke="#33a6d7" stroke-width="2"><rect x="3" y="5" width="24" height="27" rx="2"/><rect x="10" y="2" width="10" height="6"/><path d="M9 17 H21 M9 23 H21"/></svg></div></div>
  <div class="abs step-ring" style="left:854px;top:2522px"><div><svg width="32" height="34" viewBox="0 0 32 34" fill="none" stroke="#33a6d7" stroke-width="2"><rect x="3" y="2" width="20" height="30" rx="2"/><path d="M8 10 H18 M8 16 H18"/><rect x="16" y="18" width="13" height="13"/><path d="M20 25 h5 M22.5 22 v6"/></svg></div></div>
  <p class="abs step-label" style="left:202px;top:2622px">Enroll</p>
  <p class="abs step-label" style="left:498px;top:2622px">Learn New Strategies!</p>
  <p class="abs step-label" style="left:795px;top:2622px">See Results</p>
</section>

<section class="search">
  <svg class="abs" style="left:705px;top:2700px" width="495" height="530" viewBox="0 0 495 530">
    <defs><linearGradient id="couple" x1="0" y1="0" x2="1" y2="1"><stop offset="0" stop-color="#9a7a62"/><stop offset=".5" stop-color="#d6b59a"/><stop offset="1" stop-color="#f2e4d8"/></linearGradient></defs>
    <path d="M20 180 C30 60 120 0 230 5 C330 10 400 90 495 90 V330 C440 430 330 530 200 520 C90 510 10 400 20 300 Z" fill="none" stroke="#0455a3" stroke-width="1.5"/>
    <path role="img" aria-label="Photo of a young couple looking at a credit card together" fill="url(#couple)" d="M30 180 C40 70 125 10 230 15 C330 20 400 95 495 100 V330 C440 420 330 515 205 505 C100 495 20 395 30 300 Z"/>
  </svg>
  <p class="abs eyebrow" style="left:163px;top:2830px">Improve your credit score</p>
  <h2 class="abs" style="left:163px;top:2852px">Searching for a First-Class<br>Credit Repair Company?</h2>
  <p class="abs copy" style="left:163px;top:2946px;width:350px">Lorem Ipsum is simply dummy text of the printing and typesetting industry. Lorem Ipsum has been the industry's standard dummy text ever since the 1500s, when an unknown printer took a galley of typeand scrambled it to make a type specimen book.</p>
  <a class="abs btn" style="left:161px;top:3071px;width:375px;height:44px;font-size:14px" href="#">Schedule Your Credit Analysis &amp; Consultation</a>
</section>

<section class="pricing">
  <p class="abs eyebrow center" style="top:3278px">Save with our pricing packages</p>
  <h2 class="abs center" style="top:3303px;font-size:34px">Credit Repair Made Affordable</h2>
  <p class="abs copy center" style="top:3358px;left:340px;width:520px">Lorem Ipsum is simply dummy text of the printing and typesetting industry. Lorem Ipsum has been the industry's standard dummy text ever since the 1500s, when an unknown printer took a galley of typeand scrambled it to make a type specimen book.</p>
  <a class="abs btn" style="left:513px;top:3464px;width:173px;height:44px;font-size:14px" href="#">View Our Price</a>
</section>

<footer class="site-footer">
  <svg class="abs" style="left:0;top:3570px" width="1200" height="512" viewBox="0 0 1200 512">
    <defs><linearGradient id="foot" x1="0" y1="0" x2="1" y2="1"><stop offset="0" stop-color="#0455a3"/><stop offset=".6" stop-color="#1a7fc4"/><stop offset="1" stop-color="#33a6d7"/></linearGradient></defs>
    <path fill="#d7ecf7" d="M0 120 C200 100 350 130 500 140 C700 150 900 110 1200 150 V512 H0 Z"/>
    <path fill="url(#foot)" d="M0 140 C150 130 250 20 420 10 C560 0 640 60 780 70 C920 80 1050 40 1200 30 V512 H0 Z"/>
    <path fill="#d7ecf7" opacity=".9" d="M750 210 C880 170 1020 190 1200 230 V205 C1060 150 900 160 750 210 Z"/>
  </svg>
  <p class="abs" style="left:438px;top:3630px;font-family:Hind,sans-serif;font-weight:600;font-size:16px;color:var(--white)">Follow Us On</p>
  <a class="abs social" style="left:384px;top:3678px" href="#" aria-label="Social profile one"></a>
  <a class="abs social" style="left:437px;top:3678px" href="#" aria-label="Social profile two"></a>
  <a class="abs social" style="left:489px;top:3678px" href="#" aria-label="Social profile three"></a>
  <a class="abs social" style="left:541px;top:3678px" href="#" aria-label="Social profile four"></a>

  <div class="abs footer-col" style="left:163px;top:3782px;width:200px">
    <a class="brand" href="#" style="margin-bottom:14px">
      <span class="brand-mark" style="border-color:var(--white);width:44px;height:44px"></span>
      <span class="brand-name" style="color:var(--white);font-size:27px">VELTRUS<span class="brand-sub" style="font-size:9px">FINANCIAL REPAIR</span></span>
    </a>
    <p style="font-size:11px;line-height:18px;color:var(--white)">Lorem Ipsum is simply dummy text of the printing and typesetting industry. Lorem Ipsum has been the industry's standard dummy text ever since the 1500s, when an unknown printer took a galley of type and scrambled it to make a type specimen book.</p>
  </div>
  <div class="abs footer-col" style="left:388px;top:3795px">
    <h3>Quick Links</h3>
    <ul><li>Home</li><li>About Us</li><li>Services</li><li>Blog</li><li>Pricing</li><li>Contact Us</li></ul>
  </div>
  <div class="abs footer-col" style="left:613px;top:3795px">
    <h3>Services</h3>
    <ul><li>Collection Accounts</li><li>Repossessions</li><li>Charge offs</li><li>Late payments</li><li>Hard Inquiries</li><li>And More</li></ul>
  </div>
  <div class="abs footer-col" style="left:838px;top:3795px;width:220px">
    <h3>Contact Info</h3>
    <div class="contact-row"><svg width="20" height="20" viewBox="0 0 20 20" fill="none" stroke="#fff" stroke-width="1.8"><path d="M4 2 L8 2 L9 6 L7 8 C8 11 9 12 12 13 L14 11 L18 12 V16 C10 17 3 10 4 2 Z"/></svg>+1-555-010-0199</div>
    <div class="contact-row"><svg width="20" height="16" viewBox="0 0 20 16" fill="none" stroke="#fff" stroke-width="1.8"><rect x="1" y="2" width="18" height="12"/><path d="M1 2 L10 9 L19 2"/></svg>info@veltrusrepair.example</div>
    <div class="contact-row"><svg width="20" height="26" viewBox="0 0 20 26" fill="none" stroke="#fff" stroke-width="1.8"><path d="M10 24 C4 16 2 12 2 9 A8 8 0 0 1 18 9 C18 12 16 16 10 24 Z"/><circle cx="10" cy="9" r="3"/></svg><span>100 lorem ipsum dummy text<br>city, countries.</span></div>
  </div>
  <div class="abs" style="left:161px;top:4012px;width:878px;height:1px;background:rgba(255,255,255,.45)"></div>
  <p class="abs center" style="top:4038px;font-size:10.5px;color:var(--white)">Copyright©2020 <b>Veltrus Financial Repair.</b> All Rights Reserved. Terms &amp; Conditions | Privacy Policy.</p>
</footer>

</body>
</html>
```